End of the Year Postcard

Bright Harbor Allies - a non profit addressing peace and justice issues from an interfaith perspective

Industry/Entity Type

Non Profit

```html
<!DOCTYPE html>
<html lang="en">
<head>
<meta charset="utf-8">
<title>Bright Harbor Allies – Year End Postcard</title>
<link href="https://fonts.googleapis.com/css2?family=Oswald:wght@600&family=Tinos:wght@400&family=Archivo+Narrow:wght@400&display=swap" rel="stylesheet">
<style>
:root{
  --navy:#1b3f8f;
  --royal:#1f4fa8;
  --sky:#2a8ad8;
  --ink:#2a2a35;
  --paper-top:#eaf3fa;
  --paper-bot:#cfe3f2;
  --rule:#5b7fa8;
  --stamp:#8a8f96;
  --white:#ffffff;
}
*{margin:0;padding:0;box-sizing:border-box}
html,body{width:913px;height:1200px;overflow:hidden;background:#fff}
.postcard{position:relative;width:913px;height:1200px;overflow:hidden}

/* front */
.front{position:absolute;left:0;top:0;width:913px;height:587px;background:#fff;overflow:hidden}
.photo{position:absolute}
.photo--memorial{left:0;top:0;width:407px;height:587px;
  background:linear-gradient(180deg,#2d6fd6 0%,#5a9be8 38%,#5f6a5c 55%,#3a3c3a 72%,#6d6a66 100%)}
.photo--foodbank{left:444px;top:0;width:469px;height:276px;
  background:linear-gradient(180deg,#b58356 0%,#8a6a52 35%,#4b4650 70%,#6a6272 100%)}
.photo--skyline{left:420px;top:370px;width:493px;height:217px;
  background:linear-gradient(180deg,#d9e0e8 0%,#c7ccd2 35%,#d49550 55%,#5f5d66 75%,#8a8790 100%)}
.swoosh{position:absolute;left:0;top:0}

.brand-box{position:absolute;left:368px;top:265px;width:207px;height:116px;background:var(--white);
  border:2px solid #223;border-radius:14px;display:flex;align-items:center;justify-content:center;gap:8px;padding:0 10px}
.brand-name{font-family:'Tinos',serif;color:var(--navy);font-size:27px;line-height:27px}
.brand-dot{width:34px;height:34px;border-radius:50%;border:2px solid var(--navy);flex:none}

.banner{position:absolute;left:573px;top:276px;width:340px;height:95px;background:var(--royal);
  padding:8px 10px 0 10px;font-family:'Oswald',sans-serif;font-weight:600;color:var(--white);
  font-size:17.5px;line-height:29px;letter-spacing:-.2px}

/* back */
.back{position:absolute;left:0;top:605px;width:913px;height:595px;
  background:linear-gradient(180deg,var(--paper-top) 0%,var(--paper-bot) 100%)}
.back-divider{position:absolute;left:0;top:0}

.partner-row{position:absolute;left:30px;top:24px;display:flex;gap:9px;align-items:center}
.partner-brand{width:132px;height:74px;background:var(--white);border:1.5px solid #7aa6cc;
  display:flex;align-items:center;gap:6px;padding:0 8px}
.partner-brand .brand-name{font-size:17px;line-height:18px}
.partner-brand .brand-dot{width:24px;height:24px}
.badge{height:50px;background:#fff}
.badge--skyline{width:97px;background:linear-gradient(180deg,#e4f2fb,#9ccbe9);border:1px solid #c8d7e3}
.badge--script{width:108px;background:linear-gradient(180deg,#5b8fd6,#3a6fc0)}
.badge--seal{width:72px;height:72px;border-radius:50%;background:#5a4b40;border:2px solid #3a3029}
.rule{position:absolute;left:25px;top:107px;width:442px;height:2px;background:var(--rule)}

.copy{position:absolute;left:35px;top:124px;width:440px;font-family:'Tinos',serif;color:var(--ink);
  font-size:16.2px;line-height:22.6px;letter-spacing:-.45px}
.copy p{margin:0}
.lead{margin-bottom:11px!important}
.highlights-title{text-decoration:underline;margin-bottom:10px!important}
.highlights{list-style:none;margin-bottom:10px}
.highlights li{position:relative;padding-left:27px}
.highlights li::before{content:"";position:absolute;left:5px;top:8px;width:6px;height:6px;background:var(--ink);transform:rotate(45deg)}
.mailing{text-align:center;margin-top:12px;padding-right:20px}
.link{text-decoration:underline}

.address-block{position:absolute;left:553px;top:43px;font-family:'Archivo Narrow',sans-serif;
  font-size:11.6px;line-height:18.5px;color:#1e1e1e;letter-spacing:-.2px}
.stamp{position:absolute;left:745px;top:25px}
.write-line{position:absolute;left:549px;width:346px;border-top:1.5px dashed #6d7580}
</style>
</head>
<body>
<div class="postcard">

  <section class="front">
    <div class="photo photo--memorial" role="img" aria-label="Group of students posed in front of a bronze war memorial under a blue sky"></div>
    <div class="photo photo--foodbank" role="img" aria-label="Large group of youth volunteers gathered inside a food bank warehouse"></div>
    <div class="photo photo--skyline" role="img" aria-label="Youth leaders posed on a rooftop with a city skyline behind them"></div>

    <svg class="swoosh" width="913" height="587" viewBox="0 0 913 587" aria-hidden="true">
      <defs>
        <linearGradient id="swooshBlue" x1="0" x2="1">
          <stop offset="0" stop-color="#0e3a9a"/><stop offset="1" stop-color="#3ca0e6"/>
        </linearGradient>
      </defs>
      <path d="M365 0 C430 80 420 200 400 270 L440 270 C460 190 470 80 420 0 Z" fill="url(#swooshBlue)"/>
      <path d="M402 0 C460 90 455 200 430 270 L470 270 C490 180 492 80 444 0 Z" fill="#ffffff"/>
      <path d="M380 587 C410 520 430 440 440 380 L470 380 C455 450 435 520 420 587 Z" fill="url(#swooshBlue)"/>
      <path d="M405 587 C430 520 450 450 462 380 L478 380 C470 450 452 520 435 587 Z" fill="#ffffff"/>
    </svg>

    <div class="brand-box">
      <span class="brand-name">Bright Harbor Allies</span>
      <span class="brand-dot"></span>
    </div>

    <div class="banner">Please join Bright Harbor Allies in our campaign to develop the next generation of multi-faith leaders!</div>
  </section>

  <section class="back">
    <svg class="back-divider" width="913" height="595" viewBox="0 0 913 595" aria-hidden="true">
      <defs>
        <linearGradient id="dividerBlue" x1="0" y1="0" x2="0" y2="1">
          <stop offset="0" stop-color="#0b2f86"/><stop offset=".55" stop-color="#1d62c2"/><stop offset="1" stop-color="#35a8ec"/>
        </linearGradient>
      </defs>
      <path d="M472 0 L518 0 C506 150 500 330 495 575 L485 575 C490 330 492 150 472 0 Z" fill="url(#dividerBlue)"/>
    </svg>

    <div class="partner-row">
      <div class="partner-brand">
        <span class="brand-name">Bright Harbor Allies</span>
        <span class="brand-dot"></span>
      </div>
      <div class="badge badge--skyline"></div>
      <div class="badge badge--script"></div>
      <div class="badge badge--seal"></div>
    </div>
    <div class="rule"></div>

    <div class="copy">
      <p class="lead">In light of recent world events, our work in providing a place for multi-faith cooperation and service is needed now more than ever!</p>
      <p class="highlights-title">Highlights from 2015</p>
      <ul class="highlights">
        <li>3 Interfaith Youth Leadership Initiatives (Westbrook University, Linden University, CS Harbor Point)</li>
        <li>IYCHC – Interfaith Youth Council of Harbor County</li>
        <li>IYCVC – Interfaith Youth Council of Valley County</li>
        <li>Student Interfaith Film Festival</li>
        <li>Student Leadership Trip to Washington DC</li>
        <li>Abrahamic Faiths Peacemaking Initiative</li>
      </ul>
      <p>Please support our goals of interfaith cooperation, leadership development, and community service. To donate go to PayDrift, and give to <span class="link">give@brightharborallies.org</span>. Or send your donation directly to:</p>
      <p class="mailing">Bright Harbor Allies<br>418 W. Lantern Ave., Alder Falls, CA 91284<br>(555) 014-2290 &nbsp;&nbsp; <span class="link">www.brightharborallies.org</span></p>
    </div>

    <div class="address-block">Bright Harbor Allies<br>418 W. Lantern Ave.<br>Alder Falls, CA 91284</div>

    <svg class="stamp" width="150" height="100" viewBox="0 0 150 100" aria-hidden="true">
      <circle cx="110" cy="47" r="40" fill="none" stroke="var(--stamp)" stroke-width="1.5"/>
      <circle cx="110" cy="47" r="35" fill="none" stroke="var(--stamp)" stroke-width="1"/>
      <g fill="none" stroke="#555b62" stroke-width="2.4" stroke-linecap="round">
        <path d="M4 40 C16 32 26 48 38 40 S60 32 72 40"/>
        <path d="M4 50 C16 42 26 58 38 50 S60 42 72 50"/>
        <path d="M4 60 C16 52 26 68 38 60 S60 52 72 60"/>
        <path d="M12 70 C22 64 30 76 42 70"/>
      </g>
    </svg>

    <div class="write-line" style="top:279px"></div>
    <div class="write-line" style="top:341px"></div>
    <div class="write-line" style="top:400px"></div>
  </section>

</div>
</body>
</html>
```